Australia-Wide Industry Leader Bookkeeping Business Website Design Required

We need a website designed for our 10 year old bookkeeping business, Barwick & Lund. Barwick & Lund has been servicing the local & interstate communities of Australia, providing first-class BAS & Bookkeeping services with a personal touch unmatched by anyone else in the county.

What began 10 years ago as a small business focusing on family, friends and the local community, it has since grown into a well respected business with 95% of their business based solely on word of mouth and personal referrals from around Australia.

We would like to see designs that incorporate our existing brand/logo. The colours to be used on the website should be colours that work well with our logo. The design should communicate maturity, trust and confidence with a Web 2.0 look and feel.

We have produced mockups of the entire website as well as assets used in the mockups. Please reference the attached files. The mockups are an example of all the design elements that we want on each page. Designers are encouraged to use the mockups as a guideline only and for designers to use their own creativity.
Updates

This message is for new graphic designers who are considering commencing work on this project. Thank you for expressing an interest in our project. We would like to inform you that this project is close to completion as we have a number designs under very serious consideration.

We are currently in a position where we are disinterested providing feedback to improve on new designs submitted. We will provide feedback to improve new designs only if the submitted designs are very close to what we want for our website, and will only require 1 or 2 revision rounds to refine before the project completion date we will not work with designers to refine their newly submitted designs.

We feel that it is important for all designers to know the above information as we feel that your time and effort may be better spent working on another project.

Thank you for your understanding.

A big thank you for all the designs submitted. We are now in the process of selecting a design. Please be patient during this process. Thank you.

Target Market(s)

Busy Business Owners

Industry/Entity Type

Small Business

Requirements
Must have
• We require a rectangular "slide show" type feature to serve as a "teaser" to arouse the emotions of our website visitors. Each slide asks a specific question. The questions are:

- Is your paperwork in a mess?
- Do you need to get organised for the end of financial year?
- Are you sick & tired of endless amounts of paperwork & BASs?
- Do you feel frustrated & annoyed because you know your books need to be done?
- Do you lack the time & patience to get your paperwork done?
- Do you wish you had more time to do the things you enjoy doing?
- Contact Barwick & Lund today and we will transform your chaos into order.

Underneath the slide show will be a button to "Call Barwick & Lund Now - 03 5550 1827".

```html
<!DOCTYPE html>
<html lang="en">
<head>
<meta charset="utf-8">
<title>Barwick &amp; Lund – BAS &amp; Bookkeeping</title>
<link rel="stylesheet" href="https://fonts.googleapis.com/css2?family=Source+Sans+3:wght@400;600&display=swap">
<style>
:root{
  --red:#9b0e16;
  --red-dark:#7a0a10;
  --ink:#1d1d1d;
  --body:#555;
  --tick:#7fae2e;
  --page:#e6e6e6;
  --panel:#fff;
  --footer:#9c9c9c;
}
*{box-sizing:border-box;margin:0;padding:0}
html,body{width:816px;height:1200px;overflow:hidden}
body{position:relative;font-family:"Source Sans 3",sans-serif;color:var(--ink);
  background:linear-gradient(#e2e2e2,#ececec 60%,#e4e4e4)}
.abs{position:absolute}
.topbar{left:0;top:0;width:816px;height:3px;background:var(--red)}
.header{left:0;top:3px;width:816px;height:143px;background:linear-gradient(#e9e9e9,#fafafa 60%,#fff);border-bottom:1px solid #d6d6d6}
.brand{left:76px;top:29px;width:206px;height:40px;border:1px solid #333;background:#fff;display:flex;align-items:center;gap:8px;padding-left:8px}
.brand .mark{width:14px;height:14px;background:var(--red)}
.brand .name{font-size:24px;font-weight:600;color:var(--ink);letter-spacing:.3px;white-space:nowrap}
.nav{left:324px;top:41px;display:flex;gap:3px;font-size:9.5px;font-weight:600}
.nav a{color:var(--ink);text-decoration:none;padding:3px 7.5px;border-radius:3px}
.nav a.active{background:var(--red);color:#fff}
.intro{left:75px;top:94px;width:670px;font-size:12.4px;line-height:16px;color:#111}
.hero{left:0;top:146px;width:816px;height:261px;background:linear-gradient(90deg,#f6f6f6,#fff 45%);border-bottom:1px solid #ccc;overflow:hidden}
.hero-photo{position:absolute;left:380px;top:0;width:436px;height:261px;
  background:linear-gradient(90deg,rgba(255,255,255,1) 0%,rgba(220,220,220,.9) 25%,#bdbdbd 55%,#d8d8d8 80%,#efefef)}
.hero-swoosh{position:absolute;left:-40px;top:120px;width:300px;height:200px;border-radius:50%;border-top:2px solid rgba(155,14,22,.18)}
.hero h1{position:absolute;left:80px;top:64px;width:320px;font-size:23px;line-height:25px;font-weight:600;color:var(--red)}
.call{position:absolute;left:77px;top:128px;width:132px;height:34px;border-radius:17px;background:linear-gradient(#fff,#dfe9ef);box-shadow:0 0 0 3px #dce8ee,0 1px 3px rgba(0,0,0,.2);display:flex;align-items:center;padding-left:13px;font-size:14px;color:#222}
.call svg{position:absolute;right:10px;top:9px}
.dots{position:absolute;left:88px;top:245px;display:flex;gap:2.5px}
.dots span{width:8px;height:8px;border-radius:50%;background:#111}
.dots span.on{background:var(--red)}
.welcome{left:75px;top:428px;font-size:23px;font-weight:400;color:#222}
.welcome b{color:var(--red);font-weight:600}
.about{left:75px;top:462px;width:666px;font-size:9.4px;line-height:13.6px;color:var(--body);letter-spacing:.1px}
.panel{background:var(--panel);border:1px solid #d4d4d4;border-radius:3px;box-shadow:0 1px 3px rgba(0,0,0,.08)}
.tab{background:linear-gradient(var(--red),var(--red-dark));color:#fff;font-size:12px;padding-left:22px;display:flex;align-items:center;border-radius:3px 3px 3px 0;white-space:nowrap;overflow:hidden}
.tab-wrap{position:absolute}
.tab-wrap::after{content:"";position:absolute;left:0;bottom:-6px;border-top:6px solid #4a0509;border-left:13px solid transparent}
.tick{list-style:none;font-size:8.3px;color:#333}
.tick li{position:relative;padding-left:15px;height:15.7px;line-height:12px}
.tick li::before{content:"";position:absolute;left:2px;top:1px;width:4px;height:8px;border-right:2.5px solid var(--tick);border-bottom:2.5px solid var(--tick);transform:rotate(40deg)}
.dotlist{list-style:none;font-size:8.2px;color:#444}
.dotlist li{height:14.3px;padding-left:7px;position:relative}
.dotlist li::before{content:"";position:absolute;left:0;top:4px;width:3px;height:3px;border-radius:50%;background:var(--tick)}
.redline{color:var(--red);font-size:9.6px}
.map{left:518px;top:668px;width:204px;height:192px;background:radial-gradient(ellipse at 50% 50%,#9ccb4f 0%,#7fb53a 45%,#f3f3f3 72%);}
.quals li{height:23.8px;font-size:8.8px}
.strip{left:0;top:1086px;width:816px;height:76px;background:linear-gradient(#f7f7f7,#fff)}
.badge{top:1092px;background:#c9c9c9}
.footer{left:0;top:1162px;width:816px;height:38px;background:var(--footer)}
.footer p{position:absolute;left:0;width:860px;text-align:center;top:13px;font-size:9px;color:#fff}
.social{top:10px;width:19px;height:19px;border-radius:3px}
</style>
</head>
<body>
<div class="abs topbar"></div>
<header class="abs header">
  <div class="abs brand"><span class="mark"></span><span class="name">Barwick &amp; Lund</span></div>
  <nav class="abs nav">
    <a class="active" href="#">Home</a><a href="#">About Us</a><a href="#">Services</a><a href="#">Testimonials</a><a href="#">Articles</a><a href="#">Endorsements</a><a href="#">Links</a><a href="#">Contact Us</a>
  </nav>
  <p class="abs intro">For nearly 10 years Barwick &amp; Lund has been servicing the local &amp; interstate communities of Australia, providing first-class BAS &amp; Bookkeeping services with a personal touch unmatched by anyone else in the country</p>
</header>

<section class="abs hero">
  <div class="hero-swoosh"></div>
  <div class="hero-photo" role="img" aria-label="Photo of a stressed man slumped over an open book with glasses, phone and calculator on the desk"></div>
  <h1>Do you need to get organised for the end of financial year?</h1>
  <div class="call">Call us today
    <svg width="16" height="16" viewBox="0 0 16 16"><circle cx="8" cy="8" r="8" fill="#9b0e16"/><path d="M4 8h6M8 5l3 3-3 3" stroke="#fff" stroke-width="1.8" fill="none"/></svg>
  </div>
  <div class="dots"><span class="on"></span><span></span><span></span><span></span><span></span></div>
</section>

<h2 class="abs welcome">Welcome to <b>Barwick &amp; Lund</b></h2>
<p class="abs about">Having worked for a Certified Accountants firm for numerous years, Helen Barwick &amp; Grace Lund become concerned about the consistency of inaccurate books prepared by others in various organisations. As the quality of bookwork declined. The fees seemed to increase. Together they identified a need for a quality bookkeeping service that truly understood what being in business is all about and more importantly.how to correctly &amp; accurately process books according to the laws and requirments set by the National Tax Office. They wanted to give people a better alternative- thus Barwick &amp; Lund was born. What began as a samll busines focusing on family. Friends and the local community has since grown into a well respected business with 95% of their business based solely on word of mouth and personal referrals from around Australia</p>

<section class="abs panel" style="left:79px;top:570px;width:396px;height:498px"></section>
<div class="tab-wrap" style="left:66px;top:575px"><div class="tab" style="width:181px;height:24px">To Summarise</div></div>
<ul class="abs tick" style="left:86px;top:610px">
  <li>Free initial consultation</li><li>Registered BAS Agent #40512-118</li><li>Bookkeeping</li><li>BAS Preparation &amp; Logdgement</li><li>Payroll</li><li>IAS Preparation &amp; Logdgement</li>
</ul>
<ul class="abs tick" style="left:291px;top:610px">
  <li>Superannuation &amp; Workcover</li><li>Margin Scheme</li><li>Fuel Tax Credits</li><li>Offsite &amp; onsite bookkeeping</li><li>LedgerPro Software &amp; Training</li><li>Australia wide</li>
</ul>
<p class="abs redline" style="left:90px;top:713px">What makes Barwick &amp; Lund different from other Bookkeepers</p>
<ul class="abs tick" style="left:87px;top:740px;width:380px">
  <li>We guarantee the quality of our work</li><li>We have ovaer 35 years of experiemce</li><li>We have owned &amp; operated businesses for 35 years</li><li>The Barwick &amp; Lund team are investors &amp; traders</li><li>Extensive business network for your benefit</li><li>Backed by a team of accountants</li>
  <li style="height:auto;line-height:13.5px">We work with a team of elite accointants &amp; wealth creation professionals who coach us monthly in the following:</li>
</ul>
<ul class="abs dotlist" style="left:115px;top:874px">
  <li>Asset Protection</li><li>Superannuation &amp; Self Managed Superannuation Funds</li><li>Property Investing</li><li>Tax strategies. tax structures &amp; best tax savings</li>
</ul>
<ul class="abs tick" style="left:87px;top:938px;width:380px">
  <li class="redline" style="height:auto;line-height:13.5px">We understand just how important it is to help lead &amp; guide our clients from making profits to:</li>
</ul>
<ul class="abs dotlist" style="left:115px;top:983px">
  <li>Maximising profits</li><li>Wealth creation</li><li>Tax Minimisation</li><li>Asset protection</li>
</ul>
<p class="abs redline" style="left:88px;top:1045px">This is something that other bookkeepers just dont do!</p>

<section class="abs panel" style="left:508px;top:572px;width:233px;height:496px"></section>
<div class="tab-wrap" style="left:494px;top:578px"><div class="tab" style="width:182px;height:24px">Servicing All of Australia</div></div>
<p class="abs" style="left:517px;top:616px;width:216px;font-size:8px;line-height:13px;color:#666">95% of our clients come from client &amp; accountant referrals. We have clients all over Victoria. Queensland, NSW &amp; Western Australia so no matter where you are we can help</p>
<div class="abs map" role="img" aria-label="Map of Australia in green with major cities marked"></div>
<div class="tab-wrap" style="left:494px;top:864px"><div class="tab" style="width:236px;height:24px;padding-left:19px;font-size:11.3px;letter-spacing:-.2px">Qualifiactions, Memberships and Partnerships</div></div>
<ul class="abs tick quals" style="left:516px;top:903px">
  <li>Registered NTO BAS Agent</li><li>Certificate IV Financial Services</li><li>Certificate III Financial Services</li><li>Member of Guild of Chartered Bookkeepers</li><li>Platium Member of National Bookkeepers Circle</li><li>Tallyworks Professional Partner</li><li>TaxWise Partners</li>
</ul>

<div class="abs strip"></div>
<div class="abs badge" style="left:119px;width:56px;height:64px;border-radius:8px 8px 4px 4px;background:#c8c2bd" role="img" aria-label="Guild of Chartered Bookkeepers badge"></div>
<div class="abs badge" style="left:238px;width:82px;height:62px;background:#d8d2cc" role="img" aria-label="National Bookkeepers Circle badge"></div>
<div class="abs badge" style="left:371px;width:36px;height:61px;background:#2b4a7a" role="img" aria-label="TaxWise Partners badge"></div>
<div class="abs badge" style="left:474px;width:32px;height:61px;background:#cfc6c6" role="img" aria-label="Tallyworks partner badge"></div>
<div class="abs badge" style="left:570px;top:1102px;width:140px;height:32px;background:#d0d0d0" role="img" aria-label="National Tax Office badge"></div>

<footer class="abs footer">
  <span class="abs social" style="left:79px;background:#7cc6ea" role="img" aria-label="Social link"></span>
  <span class="abs social" style="left:103px;background:#4a66a0" role="img" aria-label="Social link"></span>
  <p>The contents of this site are copyright © 2012, Barwick &amp; Lund. All Rights Reserved.</p>
</footer>
</body>
</html>
```